Business Card Design

I give lessons and clinics for dressage riders
I would like the design to be an outline (with broad lines) of a dressage horse and rider with in background of whole card with print over top tan or parchment card with burgundy print

Industry/Entity Type

Business

Contact Information for Business Card

Tod Harlick
555-317-0492
Classical dressage training for the modern American
Clinics, lessons, training level -Prix St. George

Requirements
Must have
• broad lined outline of dressage horse and rider

```html
<!DOCTYPE html>
<html lang="en">
<head>
<meta charset="utf-8">
<title>Tod Harlick – Classical Dressage Business Card</title>
<link rel="stylesheet" href="https://fonts.googleapis.com/css2?family=Marcellus+SC&display=swap">
<style>
  :root {
    --card-tan: #c6bf98;
    --card-parchment: #e4d9a8;
    --card-shade: #b2ab86;
    --ink-burgundy: #4a1830;
    --rider-wine: #3f1229;
  }

  * { margin: 0; padding: 0; box-sizing: border-box; }

  html, body {
    width: 1200px;
    height: 693px;
    overflow: hidden;
    background: var(--card-tan);
  }

  .business-card {
    position: relative;
    width: 1200px;
    height: 693px;
    overflow: hidden;
    background:
      radial-gradient(ellipse 60% 70% at 30% 45%, var(--card-parchment) 0%, transparent 70%),
      radial-gradient(ellipse 45% 55% at 85% 25%, var(--card-parchment) 0%, transparent 70%),
      linear-gradient(135deg, var(--card-tan) 0%, var(--card-shade) 55%, var(--card-tan) 100%);
    font-family: "Marcellus SC", "Trajan Pro", serif;
    color: var(--ink-burgundy);
  }

  .background-motif {
    position: absolute;
    inset: 0;
    width: 100%;
    height: 100%;
  }

  .horse-and-rider {
    position: absolute;
    left: 565px;
    top: 16px;
    width: 590px;
    height: 424px;
  }

  .contact-line {
    position: absolute;
    left: 25px;
    top: 478px;
    font-size: 58px;
    line-height: 1;
    letter-spacing: 8px;
    white-space: nowrap;
  }

  .contact-line .phone-number {
    margin-left: 36px;
    letter-spacing: 13px;
  }

  .divider-rule {
    position: absolute;
    left: 34px;
    top: 558px;
    width: 1118px;
    height: 3px;
    background: var(--ink-burgundy);
  }

  .tagline {
    position: absolute;
    left: 25px;
    font-size: 30px;
    line-height: 1;
    letter-spacing: 7px;
    white-space: nowrap;
  }

  .tagline-services { top: 592px; }
  .tagline-levels { top: 640px; }
</style>
</head>
<body>
  <main class="business-card">
    <svg class="background-motif" viewBox="0 0 1200 693" role="img"
         aria-label="Large faint outline of a dressage horse and rider spanning the whole card">
      <defs>
        <radialGradient id="motif-glow" cx="45%" cy="40%" r="65%">
          <stop offset="0%" stop-color="#ece2b4" stop-opacity="0.55"/>
          <stop offset="100%" stop-color="#b5ae88" stop-opacity="0.25"/>
        </radialGradient>
      </defs>
      <rect width="1200" height="693" fill="url(#motif-glow)"/>
    </svg>

    <svg class="horse-and-rider" viewBox="0 0 590 424" role="img"
         aria-label="Broad-lined burgundy illustration of a dressage rider on a horse in extended trot">
      <defs>
        <radialGradient id="illustration-tone" cx="50%" cy="50%" r="60%">
          <stop offset="0%" stop-color="#5a2340" stop-opacity="0.32"/>
          <stop offset="100%" stop-color="#3f1229" stop-opacity="0.08"/>
        </radialGradient>
      </defs>
      <ellipse cx="295" cy="212" rx="295" ry="212" fill="url(#illustration-tone)"/>
    </svg>

    <p class="contact-line">
      <span class="contact-name">Tod Harlick</span><span class="phone-number">555-317-0492</span>
    </p>

    <div class="divider-rule"></div>

    <p class="tagline tagline-services">Classical dressage training for the modern American</p>
    <p class="tagline tagline-levels">Clinics, lessons, training level -Prix St. George</p>
  </main>
</body>
</html>
```